Facebook Ads for Leading Telemedicine Provider

Need a variation of this advertisement.

Would like to leave everything the same with white as the dominant color but test the pink circle with a different design style

Target Market(s)

Male / Female from 18-65

Industry/Entity Type

Health

Requirements
Must have
• Use the image attached and test a different background

```html
<!DOCTYPE html>
<html lang="en">
<head>
<meta charset="utf-8">
<title>Medora – Free Covid Testing at Home</title>
<link href="https://fonts.googleapis.com/css2?family=Lato:wght@700;900&display=swap" rel="stylesheet">
<style>
  :root {
    --stage-grey: #b3b3b3;
    --card-white: #ffffff;
    --brand-pink: #ffadd8;
    --blush: #f9e4ee;
    --navy: #041766;
    --ochre: #c9a33a;
    --sand: #f3dfa8;
    --slate: #55607e;
    --mint: #3fc38a;
  }
  * { margin: 0; padding: 0; box-sizing: border-box; }
  html, body {
    width: 1200px;
    height: 1200px;
    overflow: hidden;
    background: var(--stage-grey);
    font-family: "Lato", Arial, sans-serif;
  }
  .ad {
    position: absolute;
    left: 84px;
    top: 84px;
    width: 1032px;
    height: 1032px;
    background: var(--card-white);
    overflow: hidden;
  }
  .ad__backdrop {
    position: absolute;
    inset: 0;
    width: 1032px;
    height: 1032px;
  }
  .ad__brand {
    position: absolute;
    left: 94px;
    top: 82px;
    font-weight: 900;
    font-size: 62px;
    line-height: 1;
    color: var(--brand-pink);
    letter-spacing: -1px;
  }
  .ad__headline {
    position: absolute;
    left: 92px;
    top: 184px;
    font-weight: 900;
    font-size: 124px;
    line-height: 143px;
    color: var(--brand-pink);
    letter-spacing: -2px;
  }
  .ad__cta {
    position: absolute;
    left: 89px;
    top: 691px;
    width: 363px;
    height: 84px;
    border-radius: 9px;
    background: var(--navy);
    color: var(--card-white);
    font-weight: 900;
    font-size: 38px;
    letter-spacing: -1px;
    display: flex;
    align-items: center;
    justify-content: center;
    text-decoration: none;
  }
  .ad__url {
    position: absolute;
    left: 100px;
    top: 842px;
    font-weight: 700;
    font-size: 27px;
    color: var(--navy);
    white-space: nowrap;
  }
  .ad__virus-icon {
    position: absolute;
    left: 813px;
    top: 267px;
    width: 102px;
    height: 102px;
    border-radius: 50%;
    border: 3px solid var(--slate);
    background: radial-gradient(circle, var(--mint) 0 32%, #f4fbf7 34%);
  }
  .ad__illustration {
    position: absolute;
    left: 545px;
    top: 470px;
    width: 420px;
    height: 480px;
    border-radius: 24px;
    background: linear-gradient(160deg, var(--sand) 0%, var(--ochre) 55%, var(--slate) 100%);
  }
</style>
</head>
<body>
  <main class="ad">
    <svg class="ad__backdrop" viewBox="0 0 1032 1032" aria-hidden="true">
      <circle cx="920" cy="770" r="410" fill="none" stroke="var(--blush)" stroke-width="14" stroke-dasharray="2 26" stroke-linecap="round"/>
      <circle cx="900" cy="760" r="380" fill="var(--brand-pink)"/>
      <circle cx="900" cy="760" r="300" fill="none" stroke="var(--blush)" stroke-width="3" opacity="0.7"/>
      <circle cx="980" cy="110" r="34" fill="var(--blush)"/>
      <circle cx="960" cy="220" r="12" fill="var(--brand-pink)"/>
    </svg>

    <div class="ad__brand">Medora</div>

    <h1 class="ad__headline">Free Covid<br>Testing at<br>Home</h1>

    <a class="ad__cta" href="#">BOOK NOW</a>

    <p class="ad__url">https://medora.org/covid-testing</p>

    <div class="ad__virus-icon" role="img" aria-label="Crossed-out virus icon"></div>

    <div class="ad__illustration" role="img" aria-label="Illustration of a woman opening her front door to a masked health worker with a clipboard, a potted plant and a welcome mat"></div>
  </main>
</body>
</html>
```